Lantern Advisory Business Cards

We need a new layout for our business cards. We have a logo already. But we might be interested in only using the Lantern portion of the logo. It has been uploaded.

We would like cards that are not overly busy. Clean. Modern. Perhaps a gray color for one side.

On the back, we would like to have the lantern part of the logo and "Take the Leap, we've got you!"

Our business provides medics and safety training for corporate clients. Our website is www.lanternadvisoryllc.example.

Industry/Entity Type

Business

Contact Information for Business Card

We want include name, email address, cell phone, main line number, and website URL on the front. Use the following as an example: Marla Tobin, marla@lanternadvisoryllc.example, 402.318.7264 (cell), 402.947.315, and www.lanternadvisoryllc.example.

Font styles to use
Serif
Sans Serif

Requirements
Must have
• All required information. Back side logo with "Step forward, we keep you steady!"
Nice to have
• If possible, we would like to consider creating a card in a non-standard shape. Perhaps, the shape of a lantern. Just interested in understanding the option.

```html
<!DOCTYPE html>
<html lang="en">
<head>
<meta charset="utf-8">
<title>Lantern Advisory Business Cards</title>
<link rel="stylesheet" href="https://fonts.googleapis.com/css2?family=Montserrat:wght@400;600;700&display=swap">
<style>
  :root {
    --brand-blue: #0b4d9b;
    --tag-lilac: #aab6e2;
    --ink: #555a60;
    --rule: #d9d9d9;
    --paper: #ffffff;
    --backdrop: #e8e6e2;
  }
  * { box-sizing: border-box; margin: 0; padding: 0; }
  html, body { width: 1200px; height: 1000px; overflow: hidden; }
  body {
    background: var(--backdrop);
    font-family: "Montserrat", Arial, sans-serif;
    position: relative;
  }
  .card {
    position: absolute;
    left: 244px;
    width: 708px;
    height: 404px;
    box-shadow: 0 3px 10px rgba(0,0,0,0.18);
  }

  /* Back side */
  .card-back { top: 65px; background: var(--brand-blue); color: #fff; }
  .back-brand {
    position: absolute; left: 0; right: 0; top: 198px;
    text-align: center;
  }
  .back-brand .brand-name {
    font-size: 38px; font-weight: 400; line-height: 46px;
    letter-spacing: 1px; color: #e6eaf6;
  }
  .back-brand .brand-tagline {
    margin-top: 12px; font-size: 11.5px; font-weight: 600;
    letter-spacing: 9px; color: var(--tag-lilac);
  }
  .slogan {
    position: absolute; top: 338px; left: 56px; right: 56px;
    display: flex; align-items: center; gap: 14px;
    font-size: 16px; color: #fff; white-space: nowrap;
  }
  .slogan .line {
    flex: 1; height: 1px;
    background: linear-gradient(90deg, rgba(170,182,226,0), var(--tag-lilac));
  }
  .slogan .line.right {
    background: linear-gradient(90deg, var(--tag-lilac), rgba(170,182,226,0));
  }

  /* Front side */
  .card-front { top: 493px; background: var(--paper); }
  .card-front .band {
    position: absolute; left: 0; right: 0; bottom: 0; height: 13px;
    background: var(--brand-blue);
  }
  .front-brand { position: absolute; right: 46px; top: 102px; text-align: center; }
  .front-brand .brand-name {
    font-size: 22px; font-weight: 400; line-height: 28px;
    color: var(--brand-blue); letter-spacing: 0.5px;
  }
  .front-brand .brand-tagline {
    margin-top: 6px; font-size: 7.5px; font-weight: 600;
    letter-spacing: 5px; color: var(--ink);
  }
  .person-name {
    position: absolute; left: 40px; top: 224px;
    font-size: 18px; font-weight: 700; color: var(--brand-blue);
  }
  .divider {
    position: absolute; left: 40px; right: 41px; top: 256px;
    height: 1px; background: var(--rule);
  }
  .contact-list {
    position: absolute; left: 40px; top: 270px; list-style: none;
  }
  .contact-list li {
    display: flex; align-items: center; gap: 8px;
    height: 22.5px; font-size: 16px; color: var(--ink);
  }
  .contact-list svg { width: 14px; height: 14px; fill: var(--brand-blue); flex: none; }
</style>
</head>
<body>

<section class="card card-back" aria-label="Card back">
  <div class="back-brand">
    <div class="brand-name">Lantern Advisory</div>
    <div class="brand-tagline">THE STEADY SAFETY GUIDE</div>
  </div>
  <div class="slogan">
    <span class="line"></span>
    <span>Step forward, we keep you steady!</span>
    <span class="line right"></span>
  </div>
</section>

<section class="card card-front" aria-label="Card front">
  <div class="front-brand">
    <div class="brand-name">Lantern Advisory</div>
    <div class="brand-tagline">THE STEADY SAFETY GUIDE</div>
  </div>

  <div class="person-name">Marla Tobin</div>
  <div class="divider"></div>

  <ul class="contact-list">
    <li>
      <svg viewBox="0 0 14 14" aria-hidden="true"><path d="M4 0h6a1 1 0 0 1 1 1v12a1 1 0 0 1-1 1H4a1 1 0 0 1-1-1V1a1 1 0 0 1 1-1zm.5 1.5v9.5h5V1.5zM7 11.6a.8.8 0 1 0 0 1.6.8.8 0 0 0 0-1.6z"/></svg>
      402.318.7264
    </li>
    <li>
      <svg viewBox="0 0 14 14" aria-hidden="true"><path d="M1 4c0-1.5 2.7-2.5 6-2.5S13 2.5 13 4v1.2h-3V4H4v1.2H1zM3.5 6h7l2 6H1.5zM7 7.5a1.7 1.7 0 1 0 0 3.4 1.7 1.7 0 0 0 0-3.4z"/></svg>
      402.947.315
    </li>
    <li>
      <svg viewBox="0 0 14 14" aria-hidden="true"><path d="M0 3h14v8H0zm1 .8 6 4.2 6-4.2v-.3H1z"/></svg>
      marla@lanternadvisoryllc.example
    </li>
    <li>
      <svg viewBox="0 0 14 14" aria-hidden="true"><path d="M7 1a6 6 0 1 0 0 12A6 6 0 0 0 7 1zm0 1c.6 0 1.3 1.1 1.6 2.8H5.4C5.7 3.1 6.4 2 7 2zm-1.7.3C4.9 3 4.5 3.8 4.4 4.8H2.7a5 5 0 0 1 2.6-2.5zm3.4 0a5 5 0 0 1 2.6 2.5H9.6c-.1-1-.5-1.8-.9-2.5zM2.3 5.8h2V7v1.2h-2a5 5 0 0 1 0-2.4zm3 0h3.4V8.2H5.3zm4.4 0h2a5 5 0 0 1 0 2.4h-2zM2.7 9.2h1.7c.1 1 .5 1.8.9 2.5a5 5 0 0 1-2.6-2.5zm2.7 0h3.2C8.3 10.9 7.6 12 7 12s-1.3-1.1-1.6-2.8zm4.2 0h1.7a5 5 0 0 1-2.6 2.5c.4-.7.8-1.5.9-2.5z"/></svg>
      www.lanternadvisoryllc.example
    </li>
  </ul>

  <div class="band"></div>
</section>

</body>
</html>
```